Crumbs Crumbs - Home baking business needs a business card design. I sell at artisan food festivals.

A design for rebranding my baking business which serves artisan food festivals in the UK. Produce is locally sourced, homegrown or foraged, I make rustic unusual recipes. I would like a simple design using classic colours. I like green, 'Wrenby and Holt". I like chunky lettering, but very open to new ideas/designs. On the reverse side I would like a singular symbol demonstrating baking either a bowl and wooden spoon or cake and the facebook icon with CrumbsCrumbs

Reason: I would like to progress with the design by Tessa Marlow 4827305 . I misunderstood the deadline itinerary but would very much like to go ahead with your design. thanks

Target Market(s)

customers at food festivals, other small food businesses

Industry/Entity Type

Business

Contact Information for Business Card

Minimal amount of type on the card. Design to accentuate the look of my stall and style of baking . I display cakes on either old slate tiles, old palette boxes. Prices are hand written on brown luggage labels

Font styles to use
Other font styles liked:
• Blair MdiTC

Requirements
Must have
• Underneath Crumbs Crumbs i would like to have homemade by Pam somewhere on the front of the card.
Nice to have
• Clear lettering, classic colours i.e. Wrenby and Holt colour palettes.
Should not have
• Fancy, blingy, wordy,

```html
<!DOCTYPE html>
<html lang="en">
<head>
<meta charset="utf-8">
<title>Business Card</title>
<link rel="stylesheet" href="https://fonts.googleapis.com/css2?family=Jost:wght@400;500&family=PT+Sans:wght@700&display=swap">
<style>
  :root {
    --card-sage: #9fbfa4;
    --name-cream: #ece6cc;
    --ink-charcoal: #3c3e3b;
    --rule-grey: #6d7d6f;
    --mark-tone: #8aa890;
  }
  * { margin: 0; padding: 0; box-sizing: border-box; }
  html, body {
    width: 1200px;
    height: 667px;
    overflow: hidden;
    background: var(--card-sage);
  }
  .card {
    position: relative;
    width: 1200px;
    height: 667px;
    background: var(--card-sage);
  }
  .brand-mark {
    position: absolute;
    left: 542px;
    top: 124px;
    width: 102px;
    height: 26px;
    background: var(--mark-tone);
    border-radius: 13px;
  }
  .full-name {
    position: absolute;
    left: 0;
    width: 1200px;
    top: 165px;
    text-align: center;
    font-family: "Jost", sans-serif;
    font-weight: 500;
    font-size: 86px;
    line-height: 1;
    letter-spacing: 0;
    color: var(--name-cream);
    padding-left: 22px;
  }
  .occupation {
    position: absolute;
    left: 0;
    width: 1200px;
    top: 292px;
    text-align: center;
    font-family: "Jost", sans-serif;
    font-weight: 400;
    font-size: 36px;
    line-height: 1;
    letter-spacing: 17px;
    color: var(--ink-charcoal);
  }
  .divider {
    position: absolute;
    left: 303px;
    top: 373px;
    width: 576px;
    height: 1px;
    background: var(--rule-grey);
  }
  .contact {
    position: absolute;
    left: 0;
    width: 1200px;
    top: 418px;
    text-align: center;
    font-family: "PT Sans", sans-serif;
    font-weight: 700;
    font-size: 26px;
    line-height: 33px;
    letter-spacing: 1px;
    color: var(--ink-charcoal);
    list-style: none;
  }
  .contact .sep { padding: 0 16px; }
</style>
</head>
<body>
  <main class="card">
    <div class="brand-mark" role="img" aria-label="Brand symbol"></div>

    <h1 class="full-name">FULL NAME</h1>
    <p class="occupation">OCCUPATION</p>

    <div class="divider"></div>

    <ul class="contact">
      <li class="contact-address">20 STREET, TOWN, WE2 1YQ</li>
      <li class="contact-lines">NAME@EMAIL.CO.UK<span class="sep">|</span>01234 5678912</li>
      <li class="contact-web">WWW.YOURWEBSITE.COM</li>
    </ul>
  </main>
</body>
</html>
```